Torvane Facilities Business Card Design

We would now like to design business cards with the new Torvane Facilities logo

Target Market(s)

Professional

Industry/Entity Type

Professional services

Contact Information for Business Card

Employee name, title, phone number, email address, corporate office address and logo.

Font styles to use
Sans Serif

Colors
0054AA
0677BA
7BADD7
CADEEF
E8F1F8

Requirements
Must have
• My logo
Should not have
• any other pictures or images besides my logo

```html
<!DOCTYPE html>
<html lang="en">
<head>
<meta charset="utf-8">
<title>Torvane Facilities Business Card</title>
<link href="https://fonts.googleapis.com/css2?family=Arimo:wght@400;700&display=swap" rel="stylesheet">
<style>
  :root {
    --page-bg: #e6e6e4;
    --card-bg: #28292c;
    --card-edge: #0054aa;
    --brand-blue: #0a7ad8;
    --text-light: #e4e4e4;
    --divider: #bdbdbd;
  }
  * { margin: 0; padding: 0; box-sizing: border-box; }
  html, body {
    width: 1200px;
    height: 801px;
    overflow: hidden;
    background: var(--page-bg);
    font-family: "Arimo", Arial, sans-serif;
  }
  .sheet {
    position: relative;
    width: 1200px;
    height: 801px;
    display: flex;
    align-items: center;
    justify-content: center;
    gap: 40px;
  }
  .card {
    position: relative;
    width: 540px;
    height: 309px;
    background: var(--card-bg);
    border-bottom: 4px solid var(--card-edge);
    overflow: hidden;
  }

  /* Front */
  .card-front .brand {
    position: absolute;
    left: 40px;
    top: 0;
    width: 210px;
    height: 100%;
    display: flex;
    align-items: center;
    gap: 12px;
  }
  .brand-square {
    width: 34px;
    height: 34px;
    flex: none;
    background: var(--brand-blue);
  }
  .brand-name {
    color: var(--brand-blue);
    font-weight: 700;
    font-size: 24px;
    line-height: 1.1;
  }
  .card-front .divider {
    position: absolute;
    left: 262px;
    top: 60px;
    width: 1px;
    height: 190px;
    background: var(--divider);
  }
  .details {
    position: absolute;
    left: 290px;
    top: 62px;
    color: var(--text-light);
    font-size: 14px;
    line-height: 1.2;
  }
  .person-name {
    color: var(--brand-blue);
    font-weight: 700;
    font-size: 19px;
  }
  .person-title { margin-bottom: 18px; }
  .address { margin-bottom: 14px; }
  .contact-list { list-style: none; }
  .contact-list li {
    display: flex;
    align-items: center;
    gap: 8px;
    margin-bottom: 3px;
  }
  .contact-icon { width: 14px; height: 14px; flex: none; }

  /* Back */
  .card-back .brand-stack {
    position: absolute;
    right: 44px;
    top: 50%;
    transform: translateY(-50%);
    color: var(--brand-blue);
    font-weight: 700;
    font-size: 58px;
    line-height: 1.05;
    text-transform: uppercase;
    text-align: left;
  }
</style>
</head>
<body>
<main class="sheet">
  <section class="card card-front" aria-label="Business card front">
    <div class="brand">
      <span class="brand-square"></span>
      <span class="brand-name">Torvane<br>Facilities</span>
    </div>
    <div class="divider"></div>
    <div class="details">
      <p class="person-name">Daniel Hartley</p>
      <p class="person-title">Manager</p>
      <p class="address">Your address, city<br>state, ZIP 0000</p>
      <ul class="contact-list">
        <li>
          <svg class="contact-icon" viewBox="0 0 14 14" aria-hidden="true">
            <circle cx="7" cy="7" r="7" fill="var(--brand-blue)"/>
            <path d="M4.3 3.6 L5.6 3.4 L6.2 5.2 L5.4 5.9 Q6.1 7.5 7.9 8.5 L8.7 7.7 L10.5 8.3 L10.3 9.7 Q6 10.2 4.3 3.6 Z" fill="var(--card-bg)"/>
          </svg>
          <span>123-456-2100</span>
        </li>
        <li>
          <svg class="contact-icon" viewBox="0 0 14 14" aria-hidden="true">
            <rect x="1" y="3" width="12" height="8" fill="var(--brand-blue)"/>
            <path d="M1 3 L7 8 L13 3" fill="none" stroke="var(--card-bg)" stroke-width="1"/>
          </svg>
          <span>youremail@mailbox.com</span>
        </li>
        <li>
          <svg class="contact-icon" viewBox="0 0 14 14" aria-hidden="true">
            <circle cx="7" cy="7" r="6.5" fill="var(--brand-blue)"/>
            <circle cx="7" cy="7" r="4" fill="none" stroke="var(--card-bg)" stroke-width="1"/>
            <path d="M3 7 H11 M7 3 V11" stroke="var(--card-bg)" stroke-width="1"/>
          </svg>
          <span>www.yourwebsite.com</span>
        </li>
      </ul>
    </div>
  </section>

  <section class="card card-back" aria-label="Business card back">
    <p class="brand-stack">Torvane<br>Facilities</p>
  </section>
</main>
</body>
</html>
```